Welcome Center Signage/logo Design with Multicultural Relevance

We are looking to have a welcome signage/logo designed for our church lobby with either the word "welcome" or "Welcome to the Dunmore Valley Fellowship!"

This design must include our organizational logo (attached). It could (but does not need to) also include our church vision: "Our vision is to be a thriving diverse urban church sharing Christ's love and serving the needs of our local and global communities." The logo/signage will be printed on 4' x 6' stretch fabric.

This signage will then be hung up behind our welcome center...it will be one of the first things people see upon entering our building.

We are an urban multicultural church that has significant outreach into our local community, one that is quite culturally diverse. If you would like more information about our church, please visit www.dunmorevalleyfc.org.
Updates

Project Deadline Extended
Reason: We have committed to continue work with the designers on designs submitted over the last several days, and are scheduling the additional time needed to do so. Thank you!

Target Market(s)

Culturally (African American, Hispanic American, Asian American, European American) diverse millennials and iGens

Industry/Entity Type

Church

Font styles to use
Sans Serif

Requirements
Must have
• Our logo
Nice to have
• "Welcome" in many languages
Should not have
• I can't think of anything at the moment.

```html
<!DOCTYPE html>
<html lang="en">
<head>
<meta charset="utf-8">
<title>Welcome – Dunmore Valley Fellowship</title>
<link rel="stylesheet" href="https://fonts.googleapis.com/css2?family=Arimo:wght@400;700&family=Noto+Serif+TC:wght@400&display=swap">
<style>
  :root {
    --canvas: #7d7c74;
    --plum: #4e2136;
    --wine: #4a1f33;
    --brown: #7a4035;
    --slate: #4c4a66;
    --gold: #d6a843;
    --peach: #ecc08e;
    --strip: #ffffff;
    --caption: #222222;
  }
  * { margin: 0; padding: 0; box-sizing: border-box; }
  html, body {
    width: 1200px;
    height: 825px;
    overflow: hidden;
    background: var(--strip);
  }
  .sign {
    position: relative;
    width: 1200px;
    height: 825px;
    font-family: "Arimo", Arial, sans-serif;
  }
  .sign__field {
    position: absolute;
    left: 0; top: 0;
    width: 1200px;
    height: 799px;
    background: var(--canvas);
  }
  .brand {
    position: absolute;
    left: 0;
    top: 34px;
    width: 1200px;
    display: flex;
    flex-direction: column;
    align-items: center;
  }
  .brand__emblem {
    width: 390px;
    height: 390px;
    border-radius: 50%;
    background:
      radial-gradient(circle at 50% 42%, var(--peach) 0%, var(--gold) 22%, rgba(122,64,53,0.9) 48%, transparent 70%),
      radial-gradient(circle at 22% 30%, var(--slate) 0%, transparent 40%),
      radial-gradient(circle at 80% 72%, var(--brown) 0%, transparent 45%),
      var(--wine);
  }
  .brand__name {
    margin-top: 22px;
    font-weight: 700;
    font-size: 34px;
    line-height: 40px;
    color: var(--plum);
  }
  .greeting {
    position: absolute;
    left: 0;
    width: 1200px;
    text-align: center;
    color: var(--plum);
    white-space: nowrap;
    line-height: 1.15;
  }
  .greeting--latin {
    font-weight: 700;
    font-size: 49px;
  }
  .greeting--line1 { top: 531px; }
  .greeting--line2 { top: 618px; }
  .greeting--chinese {
    top: 697px;
    font-family: "Noto Serif TC", "Songti TC", serif;
    font-weight: 400;
    font-size: 46px;
  }
  .caption {
    position: absolute;
    left: 14px;
    top: 806px;
    font-size: 12px;
    color: var(--caption);
  }
</style>
</head>
<body>
  <main class="sign">
    <div class="sign__field"></div>

    <header class="brand">
      <div class="brand__emblem" role="img" aria-label="Church emblem: cross, dove, bowl and flowing cloth in a stained-glass circle"></div>
      <p class="brand__name">Dunmore Valley Fellowship</p>
    </header>

    <p class="greeting greeting--latin greeting--line1">Welcome! Bienvenido! Välkommen!</p>
    <p class="greeting greeting--latin greeting--line2">Herzlich Willkommen!</p>
    <p class="greeting greeting--chinese" lang="zh-Hant">歡迎！</p>

    <p class="caption">1-English, 2-Spanish, 3 Swedish, 4-German, 5- Chinese</p>
  </main>
</body>
</html>
```